Stationery Design Project

We need a stationery design for our Norwegian trucking company. We have existed for about 15 years and our 12 drivers uses relatively new vehicles to transport goods around in northern Norway. Long distance routes with fresh fish og food transport is our main operations.

We have already made alogo that's printed on our trucks. The logo and a picture of our trucks is attached. I think the logo i crappy, but since its already in use, changing it is not an option in this round. Still using a better colour scheme in the overall stationery and more interesting fonts is possible (altso in the logo).

Company details:
Name: Vikmarka AS
Organisation nr 983 517 608
Post adress: 8640 Brekka

I like minimalism and simplicity. I am avalibly for questions in normal GMT working hours either here or on mail: kjell@brekkafrakt.no

Reason: Hi. Im extending the deadline because I needed some time to find a vector file of our logo. Sorry for the inconvenience

Hi, and thanks for all your interest in the project. Some updates:

-          I have decided to commit to using one of the designs. Some designer will get the payment.

-          I have extended the deadline with 24 hours since I needed some time to find our firms vector logo (a slow Swedish man was holding me up)

-          We will not choose a design before the deadline. No need to rush.

-          We have received a lot of great design and think there is a need to specified the product we want to make:

o   Business Card for all our employers. I just need the design and will duplicate with the correct numbers and name myself. The information on should be: Logo, employer’s name, Phone number, email, website, Postal number and address. Use this as a template: logo, Leif Dahlberg, 47382950, Leif@brekkafrakt.no,, brekkafrakt.no, 8640 Brekka. The order and placement of the information is your creative decision.

o   Stickers to put on the goods we travel. On the sticker the should be the following information: Logo, phone number, Tekst and link: Fraktæ av Vikmarka. Ke du syns? Brekkafrakt.no/tilbakemelding (this means: Handled by Vikmarka. What do you think Brekkafrakt.no/feedback -à the link will be a feedback form). The placement the information and size is your creative decision with some stings: we have been thinking of using Prentolo for printing and see that a size about 6x6 cm, 8x5 or something like that. (with 3000 copies our budget is 200 punds). Any suggestions of other suppliers are welcome. Prentolo price calculator http://www.prentoloprints.example/digital-litho-printing/printing-labels-tags/stickers/

o   Letterhead with logo, address, phone number and organizational number.

o   Envelopes with logo,address, phone number and organizational number.

Have a nice day.

 

 

• Using the blue colour in the logo and using a similar graphic approch.

```html
<!DOCTYPE html>
<html lang="no">
<head>
<meta charset="utf-8">
<title>Vikmarka AS – stationery</title>
<link rel="stylesheet" href="https://fonts.googleapis.com/css2?family=PT+Serif:ital,wght@0,400;0,700;1,400;1,700&display=swap">
<style>
  :root {
    --board: #cbcbcb;
    --paper: #ffffff;
    --navy: #120c8c;
    --brand-blue: #2a55d0;
    --orange: #f7961a;
    --ink: #1a1a6e;
    --shadow: rgba(0, 0, 0, 0.45);
  }
  html, body {
    margin: 0;
    padding: 0;
    width: 1200px;
    height: 1000px;
    overflow: hidden;
    background: var(--board);
  }
  .board { display: block; width: 1200px; height: 1000px; }
  .sheet { filter: drop-shadow(5px 6px 5px var(--shadow)); }
  .paper { fill: var(--paper); }
  .band { fill: var(--brand-blue); }
  .swoosh { fill: var(--orange); }
  .wordmark {
    font-family: "PT Serif", serif;
    font-weight: 700;
    fill: var(--navy);
  }
  .wordmark--light { fill: var(--orange); }
  .wordmark-dot { fill: var(--brand-blue); }
  .footer-line {
    font-family: "PT Serif", serif;
    font-style: italic;
    font-size: 7.5px;
    fill: #ffffff;
  }
  .sticker-lead { font-family: "PT Serif", serif; font-weight: 700; fill: #fff; }
  .sticker-question { font-family: "PT Serif", serif; font-weight: 700; fill: #fff; }
  .sticker-link { font-family: "PT Serif", serif; font-weight: 700; font-style: italic; fill: #fff; }
  .card-name {
    font-family: "PT Serif", serif;
    font-size: 8.5px;
    letter-spacing: 2px;
    fill: var(--navy);
  }
  .card-role {
    font-family: "PT Serif", serif;
    font-style: italic;
    font-size: 7px;
    letter-spacing: 1.2px;
    fill: var(--navy);
  }
  .card-label { font-family: "PT Serif", serif; font-size: 6.5px; fill: var(--orange); }
  .card-contact {
    font-family: "PT Serif", serif;
    font-style: italic;
    font-size: 6.5px;
    letter-spacing: 0.6px;
    fill: var(--navy);
  }
</style>
</head>
<body>
<svg class="board" viewBox="0 0 1200 1000" xmlns="http://www.w3.org/2000/svg">

  <!-- Oval parcel sticker -->
  <g class="sticker sticker--oval sheet">
    <ellipse cx="780" cy="128" rx="121" ry="66" fill="#fff"/>
    <ellipse cx="780" cy="128" rx="114" ry="60" fill="var(--brand-blue)"/>
    <ellipse cx="780" cy="128" rx="108" ry="54" fill="none" stroke="var(--orange)" stroke-width="1.6"/>
    <circle cx="743" cy="88" r="4" class="wordmark-dot"/>
    <text x="785" y="93" text-anchor="middle" class="wordmark wordmark--light" font-size="15">Vikmarka</text>
    <text x="780" y="117" text-anchor="middle" class="sticker-lead" font-size="13">Fraktæ av Vikmarka.</text>
    <text x="780" y="143" text-anchor="middle" class="sticker-question" font-size="24">Ke du syns?</text>
    <text x="780" y="160" text-anchor="middle" class="sticker-link" font-size="10.5">Brekkafrakt.no/tilbakemelding</text>
  </g>

  <!-- Round parcel sticker -->
  <g class="sticker sticker--round sheet">
    <circle cx="1015" cy="117" r="76" fill="#fff"/>
    <circle cx="1015" cy="117" r="71" fill="var(--navy)"/>
    <circle cx="983" cy="88" r="3.5" class="wordmark-dot"/>
    <text x="1019" y="93" text-anchor="middle" class="wordmark wordmark--light" font-size="13">Vikmarka</text>
    <text x="1015" y="124" text-anchor="middle" class="sticker-lead" font-size="10.5">Fraktæ av Vikmarka.</text>
    <text x="1015" y="145" text-anchor="middle" class="sticker-question" font-size="18.5">Ke du syns?</text>
    <text x="1015" y="158" text-anchor="middle" class="sticker-link" font-size="7.8">Brekkafrakt.no/tilbakemelding</text>
  </g>

  <!-- Letterhead -->
  <g class="letterhead sheet" transform="translate(49 256)">
    <rect class="paper" width="490" height="690"/>
    <circle cx="354" cy="55" r="5" class="wordmark-dot"/>
    <text x="470" y="62" text-anchor="end" class="wordmark" font-size="22">Vikmarka</text>
    <path class="swoosh" d="M140,666 Q420,650 490,574 V626 Q380,662 140,666Z"/>
    <path class="band" d="M0,656 Q250,672 490,640 V690 H0Z"/>
    <text x="460" y="680" text-anchor="end" class="footer-line">8640 Brekka, Nordland, Organisation: 983 517 608, Phone: 471 62 839</text>
  </g>

  <!-- Business card, back (stack) -->
  <g class="business-card business-card--back sheet" transform="translate(740 262) rotate(15)">
    <rect x="-6" y="12" width="310" height="172" fill="var(--brand-blue)"/>
    <rect width="310" height="172" fill="var(--navy)"/>
    <circle cx="150" cy="86" r="5" class="wordmark-dot"/>
    <text x="205" y="92" text-anchor="middle" class="wordmark wordmark--light" font-size="20">Vikmarka</text>
  </g>

  <!-- Business card, front -->
  <g class="business-card business-card--front sheet" transform="translate(695 467)">
    <rect class="paper" width="311" height="178"/>
    <text x="22" y="46" class="card-name">LEIF DAHLBERG</text>
    <text x="46" y="57" class="card-role">Director, CEO</text>
    <text x="22" y="74" class="card-label">p:</text>
    <text x="46" y="74" class="card-contact">+47 47382950</text>
    <text x="22" y="82" class="card-label">e:</text>
    <text x="46" y="82" class="card-contact">leif@brekkafrakt.no</text>
    <text x="22" y="90" class="card-label">w:</text>
    <text x="46" y="90" class="card-contact">www.brekkafrakt.no</text>
    <circle cx="203" cy="50" r="4" class="wordmark-dot"/>
    <text x="288" y="56" text-anchor="end" class="wordmark" font-size="16">Vikmarka</text>
    <path class="swoosh" d="M130,156 Q280,145 311,85 V128 Q260,150 130,156Z"/>
    <path class="band" d="M0,150 Q150,160 311,140 V178 H0Z"/>
    <text x="288" y="169" text-anchor="end" class="footer-line" font-size="6.5">8640 Brekka, Nordland, Organisation: 983 517 608, Phone: 471 62 839</text>
  </g>

  <!-- Envelope -->
  <g class="envelope sheet" transform="translate(590 715)">
    <rect class="paper" width="558" height="238"/>
    <circle cx="406" cy="39" r="5" class="wordmark-dot"/>
    <text x="522" y="46" text-anchor="end" class="wordmark" font-size="22">Vikmarka</text>
    <path class="swoosh" d="M10,210 Q470,195 558,120 V172 Q420,205 10,210Z"/>
    <path class="band" d="M0,203 Q280,222 558,188 V238 H0Z"/>
    <text x="522" y="228" text-anchor="end" class="footer-line">8640 Brekka, Nordland, Organisation: 983 517 608, Phone: 471 62 839</text>
  </g>

</svg>
</body>
</html>
```